Qel Programming Video Tutorial Blog

Please be aware I am flexible with budget, I will increase it for great design thanks

A blog (wordpress) design required for video blogging teaching Qel Programming (creating ravlet apps). There are 4 pages required to be designed, the landing page where user submit their name and email (also shows an intro video), the main video blogging page (with beautiful video placeholder), a normal text blog page with big image at the top of each post and finally the portfolio page. The portfolio is where the tutor showcase all his previous developed apps and other projects to show his expertise.

The colour combination preferred are a mixture of blue and orange but we are open to other beautiful color combinations. Minimalistic design with lots of white and clare objectives for each page. The design should reflect the purpose of the website, someone who cannot read english landing on the page should immediately realise the page is made for learning to design ravlet apps.

I like curves and round corners, especially comment and portfolio pages with curves etc thanks

The blog domain will be quibnest.com

Target Market(s)

new programmer on the ravlet platform

Industry/Entity Type

Learning

Requirements
Must have
• ravlet image in the design
landing page has a video intro and Ravlet/mork image
Nice to have
• curves. round corners and circular shapes

```html
<!DOCTYPE html>
<html lang="en">
<head>
<meta charset="utf-8">
<title>Quibnest Blog</title>
<link href="https://fonts.googleapis.com/css2?family=Open+Sans:wght@300;400;600;700&family=Oswald:wght@400&display=swap" rel="stylesheet">
<style>
  :root {
    --navy: #0f2a44;
    --navy-deep: #0b2238;
    --ink: #10283f;
    --orange: #ee7623;
    --orange-dark: #b9520f;
    --blue: #1f8bd3;
    --link-blue: #3aa0dc;
    --grey-bar: #e4e4e4;
    --grey-line: #b9b9b9;
    --panel: #ebebeb;
    --text: #555a5f;
    --white: #ffffff;
  }
  * { box-sizing: border-box; margin: 0; padding: 0; }
  html, body { width: 1106px; height: 1200px; overflow: hidden; }
  body {
    position: relative;
    background: var(--navy);
    font-family: "Open Sans", Arial, sans-serif;
    color: var(--text);
  }
  .abs { position: absolute; }

  /* header */
  .site-header { position: absolute; left: 0; top: 0; width: 1106px; height: 85px;
    background: var(--grey-bar); border-bottom: 5px solid var(--grey-line); }
  .brand { position: absolute; left: 164px; top: 14px; display: flex; align-items: center; gap: 8px; }
  .brand-mark { width: 66px; height: 100px; background: var(--blue); border-radius: 8px; }
  .brand-name { font-size: 40px; font-weight: 700; color: var(--blue); margin-top: -30px; letter-spacing: -0.5px; }
  .main-nav { position: absolute; right: 166px; top: 28px; display: flex; align-items: center;
    font-size: 13px; font-weight: 700; color: var(--ink); }
  .main-nav a { color: inherit; text-decoration: none; padding: 0 9px; line-height: 33px; }
  .main-nav .is-active { background: var(--orange); color: var(--white); border: 1px solid #c85a10;
    border-radius: 3px; line-height: 31px; margin: 0 2px; }
  .main-nav .sep { color: #aaa; font-weight: 400; padding: 0 2px; }
  .main-nav .login { color: var(--orange); }

  .page-title { position: absolute; left: 162px; top: 130px; font-size: 23px; font-weight: 300; color: var(--white); }

  /* content panel */
  .content { position: absolute; left: 164px; top: 161px; width: 777px; height: 960px;
    background: var(--white); border-radius: 4px; }

  .post-title { position: absolute; left: 22px; width: 474px; font-family: "Oswald", "Arial Narrow", sans-serif;
    font-weight: 400; font-size: 30px; line-height: 31px; color: var(--ink); text-transform: uppercase; letter-spacing: 0.3px; }
  .date-ribbon { position: absolute; left: -6px; width: 108px; height: 26px; background: var(--orange);
    color: var(--white); font-family: "Oswald", "Arial Narrow", sans-serif; font-size: 13px;
    line-height: 26px; padding-left: 21px; }
  .date-ribbon::after { content: ""; position: absolute; left: 0; bottom: -5px;
    border-top: 5px solid var(--orange-dark); border-left: 6px solid transparent; }
  .post-photo { position: absolute; left: 22px; width: 474px; height: 231px; }
  .photo-team { background: linear-gradient(135deg, #e9ecef 0%, #caa28a 35%, #2a2a30 70%, #e6e1da 100%); }
  .photo-hall { background: linear-gradient(180deg, #7a1a1a 0%, #b22b2a 40%, #3a1414 65%, #140c0c 100%); }
  .post-excerpt { position: absolute; left: 22px; width: 474px; font-size: 13px; line-height: 19px; text-align: justify; }
  .read-more { position: absolute; left: 22px; font-size: 13px; color: var(--ink); text-decoration: underline; }
  .share { position: absolute; left: 22px; display: flex; align-items: center; gap: 5px; font-size: 12px; color: var(--ink); }
  .share-label { margin-right: 3px; }
  .share-btn { width: 19px; height: 19px; border-radius: 2px; }
  .share-btn.a { background: #5bc4e8; } .share-btn.b { background: #c9302c; }
  .share-btn.c { background: #3b5a98; } .share-btn.d { background: #1a84bc; }
  .comments-ribbon { position: absolute; left: 374px; width: 120px; height: 21px; }
  .comments-ribbon .band { position: absolute; left: 11px; top: 0; width: 98px; height: 21px; background: var(--orange);
    color: var(--white); font-size: 11px; text-align: center; line-height: 21px; }
  .comments-ribbon b { font-weight: 700; }
  .divider { position: absolute; left: 22px; width: 474px; height: 1px; background: #ddd; }

  /* sidebar */
  .side-heading { position: absolute; left: 517px; font-size: 19px; color: var(--orange); text-transform: uppercase; }
  .side-box { position: absolute; left: 517px; width: 246px; background: var(--panel); border-radius: 3px; }
  .bio-photo { position: absolute; left: 0; top: 0; width: 95px; height: 138px;
    background: linear-gradient(160deg, #e7e9ec 0%, #c9cdd2 45%, #1d2430 100%); }
  .bio-text { position: absolute; left: 101px; top: 13px; width: 138px; font-size: 11.5px; line-height: 16px; color: #4c5157; }
  .subscribe-title { position: absolute; left: 11px; top: 6px; font-size: 16px; color: var(--ink); }
  .email-field { position: absolute; left: 11px; top: 33px; width: 224px; height: 28px; background: var(--white);
    border: 1px solid #bbb; border-radius: 3px; font-size: 13px; font-weight: 300; color: #777; padding: 4px 10px; }
  .subscribe-btn { position: absolute; left: 11px; top: 72px; width: 223px; height: 30px; background: var(--orange);
    border: 1px solid #c85a10; border-radius: 3px; color: var(--white); font-weight: 700; font-size: 12.5px;
    text-align: center; line-height: 28px; }
  .recent-list { list-style: none; padding: 5px 15px 0 11px; }
  .recent-item { border-bottom: 1px solid #c9c9c9; padding: 2px 0 7px; margin-bottom: 7px; font-size: 11.5px; line-height: 14.5px; }
  .recent-date { color: var(--link-blue); }
  .recent-title { color: var(--ink); font-weight: 700; }
  .recent-summary { color: #3d4247; }

  /* footer */
  .site-footer { position: absolute; left: 0; top: 1138px; width: 1106px; height: 62px; border-top: 1px solid #23405c; background: var(--navy-deep); }
  .copyright { position: absolute; left: 183px; top: 23px; font-size: 11.5px; font-weight: 300; color: var(--link-blue); }
  .footer-social { position: absolute; left: 845px; top: 20px; display: flex; gap: 3px; }
  .footer-social span { width: 20px; height: 20px; border-radius: 50%; background: var(--blue); }
</style>
</head>
<body>

<header class="site-header">
  <div class="brand">
    <div class="brand-mark"></div>
    <div class="brand-name">Quibnest</div>
  </div>
  <nav class="main-nav">
    <a href="#">HOME</a>
    <a href="#">ABOUT US</a>
    <a href="#" class="is-active">BLOG</a>
    <a href="#">CONTACT US</a>
    <span class="sep">|</span>
    <a href="#" class="login">LOGIN</a>
  </nav>
</header>

<h1 class="page-title">BLOG</h1>

<main class="content">
  <article>
    <h2 class="post-title" style="top:16px">Vestibulum condimentum mi vitae diam tristique dignissim</h2>
    <div class="date-ribbon" style="top:83px">7TH JULY 2013</div>
    <div class="post-photo photo-team" style="top:117px" role="img" aria-label="Smiling business team applauding at a seminar"></div>
    <p class="post-excerpt" style="top:355px">Cras accumsan orci mauris, ut aliquam ipsum faucibus sed. Fusce quam dui, accumsan a magna in, faucibus tristique lectus. Vestibulum sapien leo, placerat quis luctus eget, auctor et justo. Vestibulum ante ipsum primis in faucibus orci luctus et ultrices posuere cubilia Curae; Duis sagittis, risus ut viverra dignissim, lectus nunc iaculis arcu, et gravida est tortor ut erat.</p>
    <a class="read-more" href="#" style="top:455px">Continue reading→</a>
    <div class="share" style="top:487px"><span class="share-label">Share</span><span class="share-btn a"></span><span class="share-btn b"></span><span class="share-btn c"></span><span class="share-btn d"></span></div>
    <div class="comments-ribbon" style="top:484px">
      <svg width="120" height="21" viewBox="0 0 120 21"><path d="M0 4 H14 V21 H0 L5 12.5 Z M120 4 H106 V21 H120 L115 12.5 Z" fill="#d8661a"/></svg>
      <div class="band"><b>20</b> COMMENTS</div>
    </div>
    <div class="divider" style="top:517px"></div>
  </article>

  <article>
    <h2 class="post-title" style="top:523px">Vitae diam tristique dignissim</h2>
    <div class="date-ribbon" style="top:557px">7TH JULY 2013</div>
    <div class="post-photo photo-hall" style="top:593px" role="img" aria-label="Speaker on a red-lit stage addressing a large conference audience"></div>
    <p class="post-excerpt" style="top:829px">Cras accumsan orci mauris, ut aliquam ipsum faucibus sed. Fusce quam dui, accumsan a magna in, faucibus tristique lectus. Vestibulum sapien leo, placerat quis luctus eget, auctor et justo. Vestibulum ante ipsum primis.</p>
    <a class="read-more" href="#" style="top:890px">Continue reading→</a>
    <div class="share" style="top:924px"><span class="share-label">Share</span><span class="share-btn a"></span><span class="share-btn b"></span><span class="share-btn c"></span><span class="share-btn d"></span></div>
    <div class="comments-ribbon" style="top:921px">
      <svg width="120" height="21" viewBox="0 0 120 21"><path d="M0 4 H14 V21 H0 L5 12.5 Z M120 4 H106 V21 H120 L115 12.5 Z" fill="#d8661a"/></svg>
      <div class="band"><b>20</b> COMMENTS</div>
    </div>
  </article>

  <aside>
    <h3 class="side-heading" style="top:16px">Blogger’s Bio</h3>
    <div class="side-box" style="top:43px;height:138px">
      <div class="bio-photo" role="img" aria-label="Portrait of the blogger in a dark suit"></div>
      <p class="bio-text">Lorem ipsum dolor sit amet, consectetur adipiscing elit. Sed quis nisi euismod, fermentum tellus a, lobortis quam. Vestibulum condimentum mi vitae diam tristique,</p>
    </div>

    <div class="side-box" style="top:193px;height:118px">
      <div class="subscribe-title">Subscribe to Quibnest Blog</div>
      <div class="email-field">Your Email Id</div>
      <div class="subscribe-btn">SUBSCRIBE NOW</div>
    </div>

    <h3 class="side-heading" style="top:328px">Recent Posts</h3>
    <div class="side-box" style="top:355px;height:326px">
      <ul class="recent-list">
        <li class="recent-item"><div class="recent-date">7th July 2013</div><div class="recent-title">Nam vulputate mauris id arcu pharetr</div><div class="recent-summary">Vivamus accumsan cursus hendrerit. Vivamus eu magna rhoncus....</div></li>
        <li class="recent-item"><div class="recent-date">7th July 2013</div><div class="recent-title">Nullam eget massa vel mi posuere venenatis sed quis</div><div class="recent-summary">Quisque adipiscing consequat nisi, nec accumsan quam venenatis ac....</div></li>
        <li class="recent-item"><div class="recent-date">7th July 2013</div><div class="recent-title">Vestibulum sapien leo, placerat quis luctus eget</div><div class="recent-summary">Vestibulum ante ipsum primis in faucibus orci luctus et ultrices....</div></li>
        <li class="recent-item"><div class="recent-date">7th July 2013</div><div class="recent-title">Fusce quam dui, accumsan a magna in</div><div class="recent-summary">Vestibulum sapien leo, placerat quis luctus eget, auctor et justo....</div></li>
      </ul>
    </div>
  </aside>
</main>

<footer class="site-footer">
  <p class="copyright">copyright 2013 . Quibnest.com. All rights reserved</p>
  <div class="footer-social"><span></span><span></span><span></span><span></span></div>
</footer>

</body>
</html>
```